Radiology Department needs a series of 3 facebook posts - similar design

We need a series of 3 posts for our facebook page, each one presenting the activity of one of 3 physicians.
The main design elements can be the same, the only thing that will change between posts will be the field of activity and name of the physician and the representative image of its activity.
If needed the design elements can be slightly different between posts for better adjustment to the representative images.
You can find as an attachment:
- Manual of institutional identity of the Hospital (Velmor Clinica)
- Our facebook cover page
- Our department video
- The representative images for each post, identified with the name of each physician
- The Institutional identity manual with the logo of "Brisa Medical School" - just for Dr Tomas Brandilo post.
So, each one of the three posts should state the name and field of activity of each physician, including somehow the corresponding representative image, and should have background innovative design elements.
Post 1:
Name of the physician: Prof. Doutor Rui Castelvo
Field of activity: Imagiologia Reumatológica e do Sistema Músculo-Esquelético
Image as an attachment
Post 2:
Name of the physician: Prof.ª Doutora Inês Barroca
Field of activity: Imagiologia Cardíaca
Image as an attachment
Post 3:
Name of the physician: Dr. Tomas Lupo
Field of activity: Tese de Doutoramento em Curso - Identificação da Lesão Cartilagínea Precoce. Com orientação do Prof. Doutor Rui Castelvo e Prof.ª Doutora Inês Sofia Carvalhal.
Image as an attachment
Just for Dr Tomas Lupo, the logo of Brisa Medical School should also be included (please check the corresponding institutional identity manual that was just added in documents).
Updates

Just for Dr Tomas Brandilo, the logo of Brisa Medical School should also be included (please check the corresponding institutional identity manual that was just added in documents).

Please note that we are just looking for 3 facebook POSTS, not facebook cover page, thanks.

Please kindly note that we are looking for facebook POST and NOT facebook cover page.

Target Market(s)

General Population

Industry/Entity Type

Health

Font styles to use
Other font styles liked:
• Check manual of institutional identity and try to approach if appropriate

Requirements
Must have
• Check project description.
Nice to have
• If the designer finds appropriate, the logo of the Hospital would be nice in all the three posts, the most simple one just stating "VelmorClinica" - please check the attached manual of institutional identity

```html
<!DOCTYPE html>
<html lang="pt">
<head>
<meta charset="utf-8">
<title>Velmor Clinica — Imagiologia, série de publicações</title>
<link rel="stylesheet" href="https://fonts.googleapis.com/css2?family=Exo+2:wght@500;600;700&family=Oswald:wght@500;600&family=Roboto+Condensed:wght@400;500;700&family=Roboto:wght@400;500;700&display=swap">
<style>
  :root{
    --teal-dark:#17566a;
    --teal:#2bb5b0;
    --teal-band:#155a6c;
    --gold:#f2b233;
    --red-dark:#7e170d;
    --red:#b62d18;
    --orange:#f6a21b;
    --orange-light:#ffc240;
    --blue-dark:#0b3ea3;
    --blue:#1f6fe3;
    --cyan:#2fb8f0;
    --ink:#1d2a33;
    --white:#ffffff;
    --board-light:#f4f4f4;
    --board-dark:#8d8d8d;
  }
  *{box-sizing:border-box;margin:0;padding:0}
  html,body{width:1200px;height:1200px;overflow:hidden}
  body{
    background:radial-gradient(ellipse at 50% 50%,var(--board-light) 0%,#d6d6d6 55%,var(--board-dark) 100%);
    font-family:"Roboto",sans-serif;
    position:relative;
  }
  .post{
    position:absolute;left:256px;width:688px;height:359px;overflow:hidden;
    box-shadow:0 4px 14px rgba(0,0,0,.18);
  }
  .post--msk{top:38px;background:linear-gradient(120deg,#ffffff 40%,#eef3f4 100%)}
  .post--cardiac{top:420px;background:linear-gradient(100deg,var(--red-dark) 0%,var(--red) 60%,#9c2312 100%)}
  .post--thesis{top:804px;background:linear-gradient(110deg,var(--blue-dark) 0%,var(--blue) 70%,#2a7fee 100%)}
  .shape{position:absolute;left:0;top:0}

  .brand{
    position:absolute;width:250px;height:76px;background:var(--white);
    border-radius:38px 0 0 38px;box-shadow:0 3px 10px rgba(0,0,0,.2);
    padding:12px 14px 0 22px;
  }
  .post--msk .brand,.post--thesis .brand{right:4px;top:10px}
  .post--cardiac .brand{left:6px;top:12px;border-radius:0 38px 38px 0;width:262px}
  .brand__row{display:flex;align-items:center;gap:10px}
  .brand__mark{width:14px;height:14px;background:var(--gold);flex:none}
  .brand__name{font-family:"Roboto",sans-serif;font-weight:700;font-size:27px;color:var(--teal-dark);letter-spacing:-.3px}
  .brand__tagline{font-family:"Roboto Condensed",sans-serif;font-size:11.5px;color:var(--ink);text-align:right;margin-top:4px;padding-right:6px}

  .msk-title{
    position:absolute;right:18px;top:136px;text-align:right;
    font-family:"Exo 2",sans-serif;font-weight:600;font-size:26px;line-height:28px;color:var(--teal-dark);
  }
  .msk-title .accent{color:var(--teal)}
  .msk-name{
    position:absolute;left:334px;right:0;top:264px;height:36px;background:var(--teal-band);
    color:var(--white);font-family:"Exo 2",sans-serif;font-weight:600;font-size:18px;
    display:flex;align-items:center;padding-left:20px;
  }
  .msk-name::after{content:"";width:7px;height:7px;border-radius:50%;background:var(--gold);margin-left:12px}
  .msk-name::before{content:"";position:absolute;right:0;top:17px;width:18px;height:2px;background:var(--gold)}
  .rule-gold{position:absolute;left:0;right:0;height:3px;background:var(--gold);bottom:10px}

  .cardiac-title{
    position:absolute;left:18px;top:124px;font-family:"Oswald",sans-serif;font-weight:600;
    font-size:47px;line-height:56px;color:var(--white);letter-spacing:.3px;
  }
  .cardiac-title .accent{color:var(--orange)}
  .cardiac-name{
    position:absolute;left:0;width:340px;top:256px;height:34px;background:var(--white);
    font-family:"Roboto",sans-serif;font-weight:500;font-size:18px;color:var(--ink);
    display:flex;align-items:center;padding-left:46px;
  }
  .cardiac-name::before{content:"";position:absolute;left:10px;top:16px;width:22px;height:2px;background:var(--gold)}
  .cardiac-name::after{content:"";position:absolute;left:30px;top:13px;width:8px;height:8px;border-radius:50%;background:var(--gold)}

  .thesis-text{
    position:absolute;left:386px;width:300px;top:134px;text-align:center;
    font-family:"Roboto Condensed",sans-serif;font-weight:500;font-size:17.5px;line-height:21.5px;color:var(--white);
  }
  .thesis-name{
    position:absolute;left:360px;right:0;top:280px;height:24px;display:flex;align-items:center;gap:14px;
    font-family:"Oswald",sans-serif;font-weight:500;font-size:21px;letter-spacing:1px;color:var(--white);
  }
  .thesis-name .line{flex:1;height:3px;background:var(--white)}
  .thesis-name .line--short{flex:none;width:36px}
  .thesis-stripe{position:absolute;left:0;right:0;bottom:0;height:18px;background:linear-gradient(90deg,var(--cyan),#5fd0ff)}
  .thesis-stripe::before{content:"";position:absolute;left:0;right:0;top:-6px;height:3px;background:var(--cyan)}
</style>
</head>
<body>

<section class="post post--msk">
  <svg class="shape" width="688" height="359" viewBox="0 0 688 359">
    <defs>
      <linearGradient id="mskImg" x1="0" y1="0" x2="1" y2="1">
        <stop offset="0" stop-color="#3a3a3a"/><stop offset=".5" stop-color="#7a7a7a"/><stop offset="1" stop-color="#111"/>
      </linearGradient>
    </defs>
    <path d="M0 0H272C344 0 366 58 366 132V232C366 314 338 359 270 359H0Z" fill="var(--teal)"/>
    <path d="M0 0H256C326 0 350 58 350 132V232C350 308 324 352 256 352H0Z" fill="#000"/>
    <g role="img" aria-label="Angiografia das mãos em escala de cinzentos">
      <path d="M0 0H256C326 0 350 58 350 132V232C350 308 324 352 256 352H0Z" fill="url(#mskImg)" opacity=".75"/>
    </g>
  </svg>
  <div class="brand">
    <div class="brand__row"><span class="brand__mark"></span><span class="brand__name">VelmorClinica</span></div>
    <div class="brand__tagline">Cuidamos de si, todos os dias</div>
  </div>
  <h2 class="msk-title">Imagiologia<br><span class="accent">Reumatológica</span> e do<br>Sistema Músculo<br>-Esquelético</h2>
  <div class="msk-name">Prof. Doutor Rui Castelvo</div>
  <div class="rule-gold"></div>
</section>

<section class="post post--cardiac">
  <svg class="shape" width="688" height="359" viewBox="0 0 688 359">
    <defs>
      <linearGradient id="cardOrange" x1="0" y1="0" x2="1" y2="1">
        <stop offset="0" stop-color="var(--orange-light)"/><stop offset="1" stop-color="var(--orange)"/>
      </linearGradient>
      <radialGradient id="heartImg" cx=".5" cy=".5" r=".55">
        <stop offset="0" stop-color="#a8321f"/><stop offset=".7" stop-color="#6e1a10"/><stop offset="1" stop-color="#e6ddd0"/>
      </radialGradient>
    </defs>
    <path d="M688 4H430C372 4 338 52 338 116V248C338 312 372 356 430 356H688Z" fill="#c9c9c9"/>
    <path d="M688 16H434C384 16 352 58 352 118V246C352 304 384 344 434 344H688Z" fill="url(#cardOrange)"/>
    <ellipse cx="534" cy="170" rx="108" ry="118" fill="url(#heartImg)" role="img" aria-label="Reconstrução 3D do coração com artérias coronárias"/>
    <rect x="0" y="346" width="688" height="3" fill="var(--gold)"/>
  </svg>
  <div class="brand">
    <div class="brand__row"><span class="brand__mark"></span><span class="brand__name">VelmorClinica</span></div>
    <div class="brand__tagline">Cuidamos de si, todos os dias</div>
  </div>
  <h2 class="cardiac-title">IMAGIOLOGIA<br><span class="accent">CARDÍACA</span></h2>
  <div class="cardiac-name">Prof. Doutora Inês Barroca</div>
</section>

<section class="post post--thesis">
  <svg class="shape" width="688" height="359" viewBox="0 0 688 359">
    <defs>
      <radialGradient id="kneeImg" cx=".5" cy=".45" r=".6">
        <stop offset="0" stop-color="#1c3fb0"/><stop offset=".6" stop-color="#0f2a8a"/><stop offset="1" stop-color="#050a22"/>
      </radialGradient>
    </defs>
    <path d="M0 0H286C350 0 378 58 378 132V240C378 316 348 344 286 344H0Z" fill="var(--white)"/>
    <path d="M0 0H274C338 0 366 58 366 132V238C366 306 338 334 274 334H0Z" fill="var(--gold)"/>
    <path d="M0 0H262C324 0 352 58 352 132V236C352 298 326 322 262 322H0Z" fill="#000"/>
    <path d="M0 0H262C324 0 352 58 352 132V236C352 298 326 322 262 322H0Z" fill="url(#kneeImg)" role="img" aria-label="Mapa paramétrico de ressonância magnética da cartilagem do joelho"/>
  </svg>
  <div class="brand">
    <div class="brand__row"><span class="brand__mark"></span><span class="brand__name">VelmorClinica</span></div>
    <div class="brand__tagline">Cuidamos de si, todos os dias</div>
  </div>
  <p class="thesis-text">Tese de Doutoramento em Curso<br>- Identificação da Lesão Cartilagínea<br>Precoce. Com orientação do<br>Prof. Doutor Rui Castelvo e<br>Prof. Doutora Inês Sofia Carvalhal.</p>
  <div class="thesis-name"><span class="line"></span><span>DR. TOMAS LUPO</span><span class="line line--short"></span></div>
  <div class="thesis-stripe"></div>
</section>

</body>
</html>
```